Zielgruppe
Für ein Ebook mit dem Titel 'Innehalten - Aufbruch ins Stille' mit dem Autorennamen Merle Vontobek benötige ich ein ansprechendes Cover.
Aufgabenstellung
Es sollte nicht zu bunt sein. Eher sinnlich und beruhigend. Erdtöne

```html
<!DOCTYPE html>
<html lang="de">
<head>
<meta charset="utf-8">
<title>Innehalten – Aufbruch ins Stille · Merle Vontobek</title>
<link href="https://fonts.googleapis.com/css2?family=Open+Sans:wght@400;500;600&family=Allura&display=swap" rel="stylesheet">
<style>
  :root {
    --paper: #efeef0;
    --forest: #234a39;
    --moss: #3e6955;
    --sage: #8fa38d;
    --fern: #5a7756;
    --haze: #dfe4e0;
    --bark: #6b5a3a;
    --gold-light: #ebd23a;
    --gold-dark: #c9aa6e;
  }
  * { margin: 0; padding: 0; box-sizing: border-box; }
  html, body {
    width: 750px;
    height: 1200px;
    overflow: hidden;
    background: var(--paper);
  }
  .cover {
    position: relative;
    width: 750px;
    height: 1200px;
    background: var(--paper);
    font-family: "Open Sans", Arial, sans-serif;
  }
  .cover__artwork {
    position: absolute;
    left: 40px;
    top: 85px;
    width: 710px;
    height: 750px;
    background:
      radial-gradient(ellipse 28% 22% at 22% 40%, #e3b89c 0%, rgba(227,184,156,0) 100%),
      radial-gradient(ellipse 30% 30% at 30% 62%, var(--bark) 0%, rgba(107,90,58,0) 100%),
      radial-gradient(ellipse 45% 40% at 55% 35%, var(--fern) 0%, rgba(90,119,86,0) 100%),
      radial-gradient(ellipse 40% 35% at 85% 45%, #4f6e63 0%, rgba(79,110,99,0) 100%),
      radial-gradient(ellipse 50% 30% at 60% 80%, #6f7f72 0%, rgba(111,127,114,0) 100%),
      linear-gradient(180deg, var(--haze) 0%, var(--sage) 55%, var(--haze) 100%);
    -webkit-mask-image: radial-gradient(ellipse 62% 55% at 60% 50%, #000 55%, transparent 100%);
    mask-image: radial-gradient(ellipse 62% 55% at 60% 50%, #000 55%, transparent 100%);
  }
  .cover__title {
    position: absolute;
    left: 0;
    width: 750px;
    top: 770px;
    text-align: center;
    font-weight: 500;
    font-size: 118px;
    line-height: 1;
    letter-spacing: 0.04em;
    color: var(--forest);
  }
  .cover__subtitle {
    position: absolute;
    left: 90px;
    top: 915px;
    display: flex;
    align-items: baseline;
    font-weight: 500;
    font-size: 40px;
    letter-spacing: 0.22em;
    color: var(--moss);
  }
  .cover__subtitle-accent {
    margin-left: 10px;
    font-family: "Allura", cursive;
    font-size: 78px;
    letter-spacing: 0;
    background: linear-gradient(90deg, var(--gold-light), var(--gold-dark));
    -webkit-background-clip: text;
    background-clip: text;
    color: transparent;
  }
  .cover__author {
    position: absolute;
    left: 0;
    width: 750px;
    top: 1108px;
    text-align: center;
    font-weight: 500;
    font-size: 44px;
    letter-spacing: 0.28em;
    color: var(--moss);
  }
</style>
</head>
<body>
  <main class="cover">
    <div class="cover__artwork" role="img" aria-label="Doppelbelichtung: Profil einer Frau mit geschlossenen Augen, deren Haar in einen Wald und einen stillen See übergeht"></div>
    <h1 class="cover__title">Innehalten</h1>
    <p class="cover__subtitle">Aufbruch ins<span class="cover__subtitle-accent">Stille</span></p>
    <p class="cover__author">MERLE VONTOBEK</p>
  </main>
</body>
</html>
```